Coffee label for coffee brand - Kettle Lane coffee

We want someone to design a label for packaging of a coffee line. The design will then be printed on stickers.

It is called Kettle Lane Coffee (logo enclosed) I want to incorporate a streetscape and the idea is that with every different coffee it will be a different colour (we have 6 varieties at the moment) with a black background. It needs to have a modern feel.

It needs to have a blank area towards the bottom for the type of coffee which we will print later on)

text to include

'Roasting exceptional coffee'

Target Market(s)

Coffee drinkers - modern feel

Font styles to use
Sans Serif

Colors
f78f20
9bcb3b
33a6d7
b768aa

Requirements
Must have
• the logo incorporated
• Space for coffee variety
• Quote' Roasting exceptional coffee'
Nice to have
• Streetscape theme incorporated - bright colour varieties (would love metallic) (on black background)

```html
<!DOCTYPE html>
<html lang="en">
<head>
<meta charset="utf-8">
<title>Kettle Lane Coffee – Label</title>
<link rel="stylesheet" href="https://fonts.googleapis.com/css2?family=Open+Sans:wght@400;600;700&display=swap">
<style>
  :root {
    --backdrop: #4a4848;
    --label-top: #6e4629;
    --label-mid: #56361f;
    --label-deep: #2e1d12;
    --band-dark: #3b2414;
    --band-light: #8a5a33;
    --bean-tone: #4d3020;
    --tagline-brown: #a8662f;
    --text-light: #f2ece6;
    --pill-bg: #f6f3ef;
    --pill-text: #2b1c12;
  }
  * { margin: 0; padding: 0; box-sizing: border-box; }
  html, body {
    width: 1200px;
    height: 857px;
    overflow: hidden;
    background: var(--backdrop);
    font-family: "Open Sans", sans-serif;
  }
  .label {
    position: absolute;
    left: 390px;
    top: 98px;
    width: 420px;
    height: 660px;
    border-radius: 26px;
    overflow: hidden;
  }
  .label-art {
    position: absolute;
    inset: 0;
  }
  .brand-name {
    position: absolute;
    left: 26px;
    top: 92px;
    width: 190px;
    color: var(--text-light);
    font-weight: 700;
    font-size: 34px;
    line-height: 1.05;
  }
  .tagline {
    position: absolute;
    left: 0;
    right: 0;
    top: 328px;
    text-align: center;
    transform: translateX(20px);
  }
  .tagline-brand {
    color: var(--tagline-brown);
    font-size: 19px;
    font-weight: 400;
  }
  .tagline-quote {
    color: var(--text-light);
    font-size: 22px;
    font-weight: 400;
    margin-top: 4px;
  }
  .variety-pill {
    position: absolute;
    right: 10px;
    bottom: 16px;
    width: 190px;
    height: 32px;
    border-radius: 16px;
    background: var(--pill-bg);
    color: var(--pill-text);
    font-size: 16px;
    font-weight: 600;
    display: flex;
    align-items: center;
    justify-content: center;
  }
</style>
</head>
<body>
  <div class="label">
    <svg class="label-art" viewBox="0 0 420 660" width="420" height="660">
      <defs>
        <linearGradient id="top-wash" x1="0" y1="0" x2="0.6" y2="1">
          <stop offset="0" stop-color="var(--label-top)"/>
          <stop offset="1" stop-color="var(--label-mid)"/>
        </linearGradient>
        <radialGradient id="bean-field" cx="0.5" cy="0.6" r="0.7">
          <stop offset="0" stop-color="var(--bean-tone)"/>
          <stop offset="1" stop-color="var(--label-deep)"/>
        </radialGradient>
      </defs>
      <rect class="label-ground" width="420" height="660" fill="url(#top-wash)"/>
      <g class="swoosh">
        <path d="M0,250 C140,200 280,120 420,30 L420,60 C290,150 150,230 0,270 Z" fill="var(--band-light)"/>
        <path d="M0,270 C150,230 290,150 420,60 L420,95 C300,175 160,250 0,300 Z" fill="var(--band-dark)"/>
        <path d="M0,210 C130,175 270,100 420,0 L420,14 C280,110 140,190 0,225 Z" fill="var(--band-dark)" opacity="0.55"/>
      </g>
      <path class="bean-field" role="img" aria-label="Roasted coffee beans scattered across the lower label"
            d="M0,300 C160,250 300,175 420,95 L420,660 L0,660 Z" fill="url(#bean-field)"/>
    </svg>

    <div class="brand-name">Kettle Lane Coffee</div>

    <div class="tagline">
      <p class="tagline-brand">Kettle Lane Coffee</p>
      <p class="tagline-quote">Roasting Exceptional Coffee</p>
    </div>

    <div class="variety-pill">For Coffee Variety</div>
  </div>
</body>
</html>
```